Cobaltine Pilates Summer Promotions

I would like to create 2 x A6 one-side flyers for my Cobaltine Pilates private yoga summer promotions. I have 2 promotions available (bring a friend for free + 4 for price of 3 package). I would like the 2 flyers to look similar in style but would like them to look different enough so they catch the eye of the customer that there are 2 different promotions available.
Attached is my PowerPoint "versions" which I created myself but would like them to be taken to the next level for professionalism and design. You do not have to follow this layout - this was just my (non-designer-mind) ideas.
The wording in the PowerPoint must be included. You are free to use all my logos and images attached in whichever way you think works best. Feel free to use other yoga/scenic imagery you find which may be suitable.

Please stick to these font options:
Logo font: Amatic
Main text font: Raleway

Colour palette in the branding guidelines attached.

Font styles to use
Other font styles liked:
• Amatic + Raleway

Requirements
Must have
• Colour palette as per attached branding guidelines
• Fonts Amatic + Raleway
• Same design style but 2 different layouts for the 2 different promotions
• My logo must be included
• Call to action to book a session
• Wording as per PowerPoint attached
• Contact details - email, phone and website
Nice to have
• Optional other relevant yoga/lavender themed imagery
• Picture of me (to build familiarity with customers)

```html
<!DOCTYPE html>
<html lang="en">
<head>
<meta charset="utf-8">
<title>Cobaltine Pilates – Private Yoga Classes Flyer</title>
<link href="https://fonts.googleapis.com/css2?family=Amatic+SC:wght@400;700&family=Raleway:wght@400;600&display=swap" rel="stylesheet">
<style>
  :root {
    --stage: #ee7a1c;
    --plum-deep: #5a4477;
    --plum: #8a6c93;
    --plum-dark: #6a4d71;
    --lilac-light: #ebe7f2;
    --lilac: #c4bada;
    --text-body: #6f6180;
    --white: #ffffff;
  }
  * { box-sizing: border-box; margin: 0; padding: 0; }
  html, body { width: 1200px; height: 900px; overflow: hidden; }
  body { background: var(--stage); position: relative; font-family: "Raleway", sans-serif; }

  .flyer {
    position: absolute; left: 300px; top: 30px; width: 600px; height: 840px;
    background: linear-gradient(180deg, var(--lilac-light) 0%, var(--lilac-light) 30%, var(--lilac) 100%);
    overflow: hidden;
  }
  .header-image {
    position: absolute; left: 0; top: 0; width: 600px; height: 250px;
    background: linear-gradient(180deg, var(--plum-deep) 0%, #8c79ad 55%, rgba(235,231,242,0) 100%);
  }
  .headline {
    position: absolute; left: 40px; top: 64px;
    font-family: "Amatic SC", sans-serif; font-weight: 700; color: var(--white);
    font-size: 58px; line-height: 1; letter-spacing: -1.5px; white-space: nowrap;
  }
  .subheadline {
    position: absolute; left: 42px; top: 128px;
    font-family: "Amatic SC", sans-serif; font-weight: 700; color: var(--white);
    font-size: 32px; line-height: 1; letter-spacing: -1px; white-space: nowrap;
  }
  .brand-badge {
    position: absolute; left: 404px; top: 31px; width: 176px; height: 176px;
    border-radius: 50%; background: var(--white);
    display: flex; align-items: center; justify-content: center;
  }
  .brand-name {
    font-family: "Raleway", sans-serif; font-weight: 600; font-size: 19px;
    color: var(--plum); text-align: center; line-height: 1.25;
  }
  .portrait {
    position: absolute; left: 431px; top: 220px; width: 126px; height: 188px;
    border: 3px solid var(--white);
    background: linear-gradient(180deg, #f4efe9 0%, #d9cbc6 55%, #7b6a82 100%);
    box-shadow: 0 2px 6px rgba(0,0,0,0.15);
  }
  .intro {
    position: absolute; left: 42px; top: 226px; width: 370px;
    font-size: 15.5px; line-height: 22px; color: var(--text-body);
    white-space: nowrap; letter-spacing: -0.2px;
  }
  .intro p + p { margin-top: 22px; }
  .price-box {
    position: absolute; left: 67px; top: 554px; width: 284px; height: 104px;
    background: var(--plum); border-radius: 16px; padding: 6px;
    box-shadow: 0 3px 6px rgba(80,60,100,0.25);
  }
  .price-box ul {
    list-style: none; height: 100%;
    border: 2px dashed var(--white); border-radius: 12px;
    padding: 11px 10px; color: var(--white); font-size: 16px; line-height: 22px;
  }
  .details {
    position: absolute; left: 414px; top: 446px; width: 168px;
    border-top: 2px dashed var(--plum-dark); border-bottom: 2px dashed var(--plum-dark);
    padding: 16px 0 18px; color: var(--plum-dark); white-space: nowrap;
  }
  .details dt { font-weight: 600; font-size: 14px; }
  .details dd { font-size: 12.5px; line-height: 17px; letter-spacing: -0.3px; }
  .details dd + dt { margin-top: 16px; }
  .call-to-action {
    position: absolute; left: 0; top: 714px; width: 600px; height: 62px;
    display: flex; align-items: center; justify-content: center; gap: 12px;
  }
  .cta-dot { width: 56px; height: 56px; border-radius: 50%; background: var(--plum); flex: none; }
  .cta-text {
    font-family: "Amatic SC", sans-serif; font-weight: 700; font-size: 46px;
    color: var(--plum-dark); letter-spacing: -1.5px; white-space: nowrap;
  }
  .contact {
    position: absolute; left: 0; top: 782px; width: 600px; text-align: center;
    font-size: 15px; line-height: 21px; color: var(--text-body);
  }
</style>
</head>
<body>
  <article class="flyer">
    <div class="header-image" role="img" aria-label="Field of lavender flowers fading into the flyer background"></div>
    <h1 class="headline">Private Yoga Classes</h1>
    <h2 class="subheadline">Bring a friend for free this summer!</h2>

    <div class="brand-badge">
      <span class="brand-name">Cobaltine<br>Pilates</span>
    </div>

    <div class="portrait" role="img" aria-label="Photo of the instructor sitting cross-legged on a yoga mat"></div>

    <div class="intro">
      <p>Going to a new yoga class can be a little<br>intimidating. Where do I put my mat?<br>Does it matter I can't even touch my toes?<br>What language will they speak?<br>I get it. I've been there.</p>
      <p>So instead, how about trying private yoga<br>classes? We can practice at the best time<br>for your schedule. And make it even more<br>fun by doing it with your friend.</p>
      <p>This summer if you book a private class<br>with me you can now do just that, and<br>bring a friend along for free!</p>
    </div>

    <div class="price-box">
      <ul>
        <li>60 minutes – 120fr (60fr each!)</li>
        <li>75 minutes – 150fr (75fr each!)</li>
        <li>90 minutes – 180fr (90fr each!)</li>
      </ul>
    </div>

    <dl class="details">
      <dt>Offer period:</dt>
      <dd>July to September 2017</dd>
      <dt>Location:</dt>
      <dd>Let's discuss! I have<br>options to use studio<br>spaces or we can do it at<br>yours' or your friend's<br>home.</dd>
    </dl>

    <div class="call-to-action">
      <span class="cta-dot"></span>
      <span class="cta-text">Get in touch to book your session!</span>
      <span class="cta-dot"></span>
    </div>

    <div class="contact">
      <p>0761 318 274 | mira_cobaltine@mailbox.com</p>
      <p>www.cobaltine.studio</p>
    </div>
  </article>
</body>
</html>
```